Rise As Captain Book Cover Design

Book Cover Design Brief
Book Title
Rise As Captain
Subtitle
The 10 Quiet Habits of Remarkable Command
Author
Orwen Dalquist
Overview
This book is about leadership that starts within.
Most leadership books focus on tactics or management strategies. This book focuses on the inner disciplines that create powerful leaders — mindset, integrity, focus, empathy, professionalism, honesty, and self-respect.
The tone of the book is bold, direct, confident, and transformational.
This is not a soft or corporate leadership book. It is a call to step up and become the leader you are capable of becoming.
The cover should feel:
• Powerful
• Professional
• Transformational
• Premium
• Memorable
Think best-selling leadership book, not a generic business book.
Target Audience
Business owners
Managers
Entrepreneurs
Team leaders
Professionals who want to grow as leaders
Most readers are ambitious professionals who want to level up their leadership and life.
Design Direction
The design should communicate:
Strength. Discipline. Leadership. Personal transformation.
Avoid cliché leadership visuals like:
• Handshakes
• Office buildings
• Corporate stock imagery
• Teams sitting around tables
The design should feel iconic, bold, and timeless.
Think about covers of successful leadership books such as:
Copper Rituals
Total Stewardship
Won't Break Now
Begin From Purpose
The 36 Rules of Sway
These covers are simple, powerful, and recognizable even at small sizes.
Typography
The title RISE AS CAPTAIN should be:
• Bold
• Strong
• Dominant on the cover
• Easy to read even at small sizes (important for Vellora thumbnails)
The subtitle should be clean and secondary to the title.
The overall typography should feel strong, modern, and premium.
Color Direction
Designers are free to explore colors, but the cover should feel strong and premium, not playful.
Colors that often work well for leadership books include:
Black
Gold
White
Deep blue
Dark red
High contrast and clarity are important.
Style
Preferred style:
• Clean
• Modern
• Minimal
• Strong contrast
Avoid clutter and overly busy designs.
The goal is to create a cover that feels powerful and professional at first glance.
Deliverables
Front cover design for a leadership book.
Final files should include:
• High resolution artwork
• Editable source files
• Print-ready version suitable for publishing
Goal of the Cover
When someone sees this book on Vellora or in a bookstore, they should immediately think:
“This looks like a serious leadership book.”
The design should feel like it belongs next to books by authors such as:
Marcus Thorley
Brandt Osgood
Peter Hollis
Nolan Fairbrook
A strong, confident cover that attracts leaders who want to grow and perform at a higher level.
Target Market(s)
Business Owners and High level managers
Look and feel
Each slider illustrates characteristics of the customer's brand and the style your logo design should communicate.

```html
<!DOCTYPE html>
<html lang="en">
<head>
<meta charset="UTF-8">
<title>Rise As Captain — Book Cover</title>
<link href="https://fonts.googleapis.com/css2?family=Montserrat:wght@700;800;900&family=Oswald:wght@500;600&display=swap" rel="stylesheet">
<style>
  :root {
    --page: #ffffff;
    --cover-black: #0d0d0d;
    --pattern-black: #161616;
    --gold-light: #f3cf6a;
    --gold: #d9a93a;
    --gold-deep: #a87a1f;
    --white: #ffffff;
  }
  html, body {
    margin: 0;
    padding: 0;
    width: 1200px;
    height: 1200px;
    overflow: hidden;
    background: var(--page);
  }
  .canvas {
    position: relative;
    width: 1200px;
    height: 1200px;
    background: var(--page);
  }
  .cover {
    position: absolute;
    left: 222px;
    top: 31px;
    width: 763px;
    height: 1110px;
    background: var(--cover-black);
    overflow: hidden;
    box-shadow: 0 2px 6px rgba(0,0,0,0.25);
  }
  .cover-texture {
    position: absolute;
    left: 0;
    right: 0;
    top: 500px;
    bottom: 0;
    background: linear-gradient(180deg, var(--cover-black) 0%, var(--pattern-black) 25%, var(--pattern-black) 100%);
  }
  .title {
    position: absolute;
    left: 0;
    right: 0;
    top: 72px;
    margin: 0;
    text-align: center;
    font-family: "Montserrat", sans-serif;
    font-weight: 800;
    font-size: 128px;
    line-height: 138px;
    letter-spacing: 1px;
    background: linear-gradient(180deg, var(--gold-light) 0%, var(--gold) 55%, var(--gold-deep) 100%);
    -webkit-background-clip: text;
    background-clip: text;
    color: transparent;
  }
  .subtitle {
    position: absolute;
    left: 0;
    right: 0;
    top: 362px;
    margin: 0;
    text-align: center;
    font-family: "Oswald", sans-serif;
    font-weight: 600;
    font-size: 54px;
    line-height: 62px;
    letter-spacing: 1px;
    color: var(--white);
    text-transform: uppercase;
  }
  .subtitle .accent { color: var(--gold); }
  .emblem {
    position: absolute;
    left: 187px;
    top: 541px;
    width: 397px;
    height: 416px;
    border-radius: 50%;
    background: radial-gradient(circle at 50% 50%, var(--gold-light) 0%, var(--gold) 20%, rgba(168,122,31,0.45) 42%, rgba(22,22,22,0) 68%);
  }
  .author {
    position: absolute;
    left: 0;
    right: 0;
    top: 988px;
    margin: 0;
    text-align: center;
    font-family: "Montserrat", sans-serif;
    font-weight: 700;
    font-size: 52px;
    letter-spacing: 2px;
    color: var(--white);
    line-height: 1;
  }
</style>
</head>
<body>
  <div class="canvas">
    <div class="cover">
      <div class="cover-texture" role="img" aria-label="Subtle embossed geometric triangle pattern in dark black"></div>
      <h1 class="title">RISE AS<br>CAPTAIN</h1>
      <p class="subtitle">The <span class="accent">10 Quiet Habits</span><br>of Remarkable <span class="accent">Command</span></p>
      <div class="emblem" role="img" aria-label="Glowing gold compass star emblem with a ring of points"></div>
      <p class="author">ORWEN DALQUIST</p>
    </div>
  </div>
</body>
</html>
```